Business card design needed for rebranded top-end landscaping business

We need a new business card design, incorporating our logo (colours Green #8dc63f and Grey #8a8c8e) and also some options that include the colour dark navy (eg #000040) as our uniforms are navy with white and grey trim.

We are an innovative landscaping company that maintains high-end gardens for meticulous clients. We pride ourselves on our customer service, our professionalism, and our workmanship.

Our business name needs to be easily read and our branding needs to be bold and memorable, without screaming "tradesman"! We prefer clean lines over lots of fine detail.

The design MUST include:
- Business name ("Brambleton Gardenworks")
- Logo (file uploaded)
- Employee name
- Phone number
- Email address
- www.brambletongardenworks.com.au
- Facebook & Instagram logos
- The Turfcraft Guild logo (file uploaded) along with the word "Member"
- Licence "Lic. 618392K"

OPTIONAL inclusions:
- "Creating outdoor spaces for our community to be inspired, refreshed and re-energised"
- "Landscape Maintenance - Irrigation - Arboriculture" (dashes can be replaced with dots or other)
- "Fully qualified, licensed & insured"
- "Residential - Strata - Commercial - Real Estate" (dashes can be replaced with dots or other)

High-end professionals and retirees, real estate agents

Landscaping

See Project description

Sans Serif

Designer to choose colors to be used in the design.

• Must incorporate our logo, and colours Green #8dc63f and Grey #8a8c8e) from the logo, and the colour DARK NAVY (eg #000040).
• The design MUST include:
• - Business name ("Brambleton Gardenworks")
• - Logo (file uploaded)
• - Employee name
• - Phone number
• - Email address
• - www.brambletongardenworks.com.au
• - Facebook & Instagram logos
• - The Turfcraft Guild logo (file uploaded) along with the word "Member"
• - Licence "Lic. 618392K"
• OPTIONAL inclusions:
• - "Creating outdoor spaces for our community to be inspired, refreshed and re-energised"
• - "Landscape Maintenance - Irrigation - Arboriculture" (dashes can be replaced with dots or other)
• - "Fully qualified, licensed & insured"
• - "Residential - Strata - Commercial - Real Estate" (dashes can be replaced with dots or other)

```html
<!DOCTYPE html>
<html lang="en">
<head>
<meta charset="utf-8">
<title>Brambleton Gardenworks – Business Card</title>
<link href="https://fonts.googleapis.com/css2?family=Lato:wght@400;700;900&display=swap" rel="stylesheet">
<style>
  :root {
    --backdrop: #2b2b2d;
    --navy: #04042e;
    --navy-deep: #000026;
    --navy-pattern: #0b0c3a;
    --green: #8dc63f;
    --grey: #8a8c8e;
    --rule: #4a4c6a;
    --white: #ffffff;
  }
  * { margin: 0; padding: 0; box-sizing: border-box; }
  html, body { width: 1200px; height: 1108px; overflow: hidden; }
  body {
    background: var(--backdrop);
    font-family: 'Lato', sans-serif;
    position: relative;
  }
  .card {
    position: absolute;
    top: 214px;
    width: 420px;
    height: 680px;
    border-radius: 26px;
    background: var(--navy);
    box-shadow: 0 18px 40px rgba(0,0,0,.45);
    overflow: hidden;
    display: flex;
    flex-direction: column;
    align-items: center;
  }
  .card--front { left: 150px; }
  .card--back { left: 630px; }

  /* front */
  .brand {
    margin-top: 150px;
    display: flex;
    align-items: center;
    gap: 12px;
  }
  .brand__dot {
    width: 34px; height: 34px; border-radius: 50%;
    background: var(--green);
    flex: none;
  }
  .brand__name {
    font-weight: 900;
    font-size: 27px;
    line-height: 1.05;
    color: var(--grey);
  }
  .brand-rule {
    margin-top: 14px;
    width: 300px;
    height: 3px;
    background: var(--green);
  }
  .employee {
    margin-top: 34px;
    font-weight: 900;
    font-size: 26px;
    letter-spacing: .5px;
    color: var(--green);
    text-transform: uppercase;
  }
  .icon-row {
    margin-top: 14px;
    display: flex;
    align-items: center;
    gap: 8px;
  }
  .icon-row__line { width: 64px; height: 1px; background: var(--rule); }
  .icon {
    width: 30px; height: 30px; border-radius: 50%;
    background: var(--green);
    display: flex; align-items: center; justify-content: center;
  }
  .contact {
    margin-top: 12px;
    text-align: center;
    color: var(--white);
    font-size: 19px;
    line-height: 1.35;
  }
  .guild-row {
    margin-top: 32px;
    display: flex;
    align-items: center;
    gap: 18px;
  }
  .guild-row__line { width: 90px; height: 1px; background: var(--rule); }
  .guild-badge {
    width: 40px; height: 40px;
    border: 3px solid var(--green);
    border-radius: 6px;
  }
  .guild-name {
    margin-top: 10px;
    color: var(--white);
    font-size: 20px;
    letter-spacing: 3px;
    text-transform: uppercase;
  }
  .member {
    margin-top: 6px;
    color: var(--green);
    font-weight: 700;
    font-size: 21px;
    text-transform: uppercase;
  }

  /* back */
  .pattern-field {
    position: absolute;
    inset: 0 0 150px 0;
    background: linear-gradient(180deg, var(--navy-pattern), var(--navy));
  }
  .back-mark {
    position: absolute;
    top: 290px;
    left: 0; right: 0;
    display: flex;
    justify-content: center;
    align-items: center;
    gap: 8px;
  }
  .back-mark__dot {
    width: 22px; height: 22px; border-radius: 50%;
    background: var(--green);
  }
  .back-mark__name {
    font-weight: 900;
    font-size: 15px;
    color: var(--grey);
  }
  .social-row {
    position: absolute;
    bottom: 112px;
    left: 0; right: 0;
    display: flex;
    justify-content: center;
    align-items: center;
    gap: 8px;
  }
  .social-row__line { width: 42px; height: 1px; background: var(--rule); }
  .social {
    width: 30px; height: 30px; border-radius: 50%;
    border: 2px solid var(--green);
  }
  .licence {
    position: absolute;
    bottom: 74px;
    left: 0; right: 0;
    text-align: center;
    color: var(--grey);
    font-weight: 700;
    font-size: 20px;
    text-transform: uppercase;
  }
</style>
</head>
<body>

<section class="card card--front">
  <div class="brand">
    <span class="brand__dot"></span>
    <span class="brand__name">Brambleton<br>Gardenworks</span>
  </div>
  <div class="brand-rule"></div>

  <h1 class="employee">Daniel Harper</h1>

  <div class="icon-row">
    <span class="icon-row__line"></span>
    <span class="icon" aria-label="Phone">
      <svg width="16" height="16" viewBox="0 0 16 16"><path d="M4 1.5 6 4.5 4.8 6.2c.9 1.9 2.3 3.3 4.2 4.2L10.7 9.2l3 2-1.2 2.6C7 13.5 2.5 9 2.2 3.4Z" fill="#04042e"/></svg>
    </span>
    <span class="icon" aria-label="Email">
      <svg width="16" height="16" viewBox="0 0 16 16"><rect x="2" y="4" width="12" height="8" rx="1" fill="#04042e"/><path d="M2.5 4.5 8 9l5.5-4.5" fill="none" stroke="#8dc63f" stroke-width="1.2"/></svg>
    </span>
    <span class="icon" aria-label="Website">
      <svg width="16" height="16" viewBox="0 0 16 16"><path d="M8 1.5a4.5 4.5 0 0 0-4.5 4.5C3.5 9.5 8 14.5 8 14.5s4.5-5 4.5-8.5A4.5 4.5 0 0 0 8 1.5Z" fill="#04042e"/><circle cx="8" cy="6" r="1.7" fill="#8dc63f"/></svg>
    </span>
    <span class="icon-row__line"></span>
  </div>

  <p class="contact">
    044-987 654 321<br>
    hello@brambletonmail.com<br>
    www.brambletongardenworks.com.au
  </p>

  <div class="guild-row">
    <span class="guild-row__line"></span>
    <span class="guild-badge" role="img" aria-label="Guild membership badge"></span>
    <span class="guild-row__line"></span>
  </div>
  <p class="guild-name">The Turfcraft Guild</p>
  <p class="member">Member</p>
</section>

<section class="card card--back">
  <div class="pattern-field" role="img" aria-label="Faint repeating brand pattern in dark navy"></div>
  <div class="back-mark">
    <span class="back-mark__dot"></span>
    <span class="back-mark__name">Brambleton Gardenworks</span>
  </div>
  <div class="social-row">
    <span class="social-row__line"></span>
    <span class="social" role="img" aria-label="Social profile one"></span>
    <span class="social" role="img" aria-label="Social profile two"></span>
    <span class="social-row__line"></span>
  </div>
  <p class="licence">Lic. 618392K</p>
</section>

</body>
</html>
```